Erotik Online Shop
Zielgruppe
Kunden des Online Shops, vorzugsweise schwule Männer wobei der Shop auch die hetero Ziegruppe bedienen bzw. befriedigen kann.
Aufgabenstellung
Für den Relounch unserers Online Shops benötigen wir mehrer Grafiken für die Startseite des Shops sowie eventuell einen Überabreitung unseres Logos.

```html
<!DOCTYPE html>
<html lang="de">
<head>
<meta charset="utf-8">
<title>Flirtwerk7 – Startseitengrafik</title>
<link rel="stylesheet" href="https://fonts.googleapis.com/css2?family=Anton&family=Arimo:wght@700&display=swap">
<style>
  :root {
    --bg-dark: #050505;
    --bg-mid: #2a2a2a;
    --bg-light: #4a4a4a;
    --flame-core: #ffd34a;
    --flame-mid: #f26a10;
    --flame-edge: #8a1a04;
    --band: rgba(130, 130, 130, 0.45);
    --text-light: #ffffff;
    --ghost: rgba(255, 255, 255, 0.06);
  }
  html, body {
    margin: 0;
    padding: 0;
    width: 1200px;
    height: 655px;
    overflow: hidden;
    background: #ffffff;
  }
  .banner {
    position: relative;
    width: 1200px;
    height: 655px;
    border-radius: 22px;
    overflow: hidden;
    background: linear-gradient(105deg, var(--bg-dark) 0%, var(--bg-dark) 30%, var(--bg-mid) 65%, var(--bg-light) 100%);
  }
  .flame-art {
    position: absolute;
    left: 250px;
    top: 0;
    width: 340px;
    height: 655px;
  }
  .ghost-name {
    position: absolute;
    right: 40px;
    top: 60px;
    font-family: "Anton", "Arial Narrow", sans-serif;
    font-size: 150px;
    line-height: 1;
    color: var(--ghost);
    margin: 0;
  }
  .brand-name {
    position: absolute;
    left: 34px;
    top: 200px;
    margin: 0;
    font-family: "Anton", "Arial Narrow", sans-serif;
    font-size: 96px;
    line-height: 1;
    color: var(--text-light);
    letter-spacing: 1px;
  }
  .url-band {
    position: absolute;
    left: 0;
    top: 470px;
    width: 1200px;
    height: 73px;
    background: var(--band);
    display: flex;
    align-items: center;
    justify-content: flex-end;
    box-sizing: border-box;
    padding-right: 50px;
  }
  .url-band__text {
    font-family: "Arimo", Arial, sans-serif;
    font-weight: 700;
    font-size: 40px;
    letter-spacing: 17px;
    color: var(--text-light);
  }
</style>
</head>
<body>
  <main class="banner">
    <p class="ghost-name" aria-hidden="true">Flirtwerk7</p>

    <svg class="flame-art" viewBox="0 0 340 655" role="img" aria-label="Foto eines lodernden Feuers mit hoch aufschlagenden Flammen">
      <defs>
        <radialGradient id="flameGlow" cx="0.5" cy="0.75" r="0.6">
          <stop offset="0" stop-color="var(--flame-core)"/>
          <stop offset="0.45" stop-color="var(--flame-mid)"/>
          <stop offset="0.85" stop-color="var(--flame-edge)" stop-opacity="0.6"/>
          <stop offset="1" stop-color="var(--flame-edge)" stop-opacity="0"/>
        </radialGradient>
      </defs>
      <rect width="340" height="655" fill="url(#flameGlow)"/>
    </svg>

    <h1 class="brand-name">Flirtwerk7</h1>

    <div class="url-band">
      <span class="url-band__text">www.flirtwerk7.de</span>
    </div>
  </main>
</body>
</html>
```